New Website - Harbinwell Press
Create A New Homepage Design
New Website - Harbinwell Press - Publishing
Creative Brief
Publishing
Harbinwell Press is a new division of our existing Harbinwell Classbooks business (see www.harbinwellclassbooks.example)
We provide book publishing and printing services primarily focused on the Education industry.
I'm looking to create a new website that people who are interested in printing text books and childrens books would be comfortable using. These would be teachers, academic professionals, students, and aspiring children's book authors.
Colorful
Red (#aa0000)
Lime Green (#75A514)
Gray (#cccccc)
http://www.pollquarry.example/
http://www.bright-tin.example/
http://www.pagolo.example/
We are looking for a design of both the Logo and the website. The Logo should be in the red described above. I'd like to see a simple design featuring the following main navigation items - Make Books - View Library - Pricing - Contact Us There should be a section on the homepage for - News & Announcements - This Month's Promotion - Request Information

```html
<!DOCTYPE html>
<html lang="en">
<head>
<meta charset="utf-8">
<title>Harbinwell Press — Book Publishing &amp; Printing Services</title>
<link href="https://fonts.googleapis.com/css2?family=PT+Sans:wght@400;700&amp;family=Open+Sans:wght@400;600;700&amp;display=swap" rel="stylesheet">
<style>
  :root{
    --red:#aa0000;
    --red-deep:#7a0000;
    --red-bright:#c8120f;
    --lime:#75a514;
    --lime-light:#a6d22e;
    --lime-dark:#4d7a08;
    --gray:#cccccc;
    --gray-bg:#d9d9d9;
    --paper:#ffffff;
    --ink:#333333;
    --ink-soft:#555555;
    --footer:#1e1e1e;
    --orange:#f2a20c;
  }
  *{box-sizing:border-box;margin:0;padding:0}
  html,body{width:1200px;height:971px;overflow:hidden}
  body{
    position:relative;
    font-family:"Open Sans",Arial,sans-serif;
    color:var(--ink);
    background:linear-gradient(180deg,var(--gray-bg) 0%,#c8c8c8 100%);
  }
  a{text-decoration:none}
  .header-band{
    position:absolute;left:0;top:0;width:1200px;height:265px;
    background:radial-gradient(ellipse at 50% 0%,var(--red-bright) 0%,var(--red) 45%,var(--red-deep) 100%);
  }
  .brand{position:absolute;left:105px;top:38px;display:flex;align-items:center;gap:14px}
  .brand-mark{width:40px;height:40px;background:var(--lime)}
  .brand-name{font-family:"PT Sans",sans-serif;font-size:31px;color:#fff;letter-spacing:1px;line-height:1}
  .brand-tagline{font-family:"PT Sans",sans-serif;font-size:15px;color:#f4d36a;letter-spacing:1px;margin-top:4px}
  .call{position:absolute;right:110px;top:18px;text-align:right;color:#fff}
  .call-label{font-family:"PT Sans",sans-serif;font-size:16px;color:#f4d36a}
  .call-number{display:flex;align-items:center;gap:8px;font-family:"PT Sans",sans-serif;font-weight:700;font-size:34px;line-height:1.1}
  .main-nav{position:absolute;left:598px;top:102px;display:flex;gap:8px}
  .main-nav a{font-family:"Open Sans",sans-serif;font-weight:700;font-size:14px;color:#fff;padding:5px 14px;border-radius:14px}
  .main-nav a.active{background:#fff;color:var(--red)}

  .showcase{
    position:absolute;left:97px;top:153px;width:981px;height:281px;
    background:linear-gradient(180deg,var(--lime-light) 0%,var(--lime) 55%,var(--lime-dark) 100%);
    border-radius:6px;box-shadow:0 4px 10px rgba(0,0,0,.35);
  }
  .slide-photo{position:absolute;left:21px;top:13px;width:592px;height:255px;border-radius:4px;
    background:linear-gradient(135deg,#b9b9b9 0%,#d65a6a 40%,#8e2434 65%,#5a5a5a 100%)}
  .slide-arrow{position:absolute;top:115px;width:24px;height:24px;background:rgba(40,40,40,.7)}
  .slide-arrow.prev{left:21px}.slide-arrow.next{left:589px}
  .slide-dots{position:absolute;left:280px;top:246px;display:flex;gap:8px}
  .slide-dots span{width:10px;height:10px;border-radius:50%;background:#fff;opacity:.75}
  .slide-dots span:first-child{opacity:1}
  .showcase-copy{position:absolute;left:632px;top:18px;width:335px;color:#fff}
  .showcase-copy h1{font-family:"PT Sans",sans-serif;font-weight:400;font-size:26px;line-height:1.12;color:#eaff7a;text-shadow:0 1px 2px rgba(0,0,0,.3);letter-spacing:-.2px}
  .showcase-copy p{font-size:12px;line-height:1.45;margin-top:10px}
  .cta{position:absolute;top:224px;height:46px;display:flex;align-items:center;justify-content:center;
    font-family:"PT Sans",sans-serif;font-size:19px;color:#fff;border-radius:4px;box-shadow:0 2px 3px rgba(0,0,0,.3)}
  .cta.tour{left:632px;width:130px;background:linear-gradient(#ffc23a,var(--orange))}
  .cta.sample{left:772px;width:196px;background:linear-gradient(#8ec428,var(--lime-dark));border:1px solid #dff59a}

  .content{position:absolute;left:97px;top:468px;width:981px;height:322px;background:var(--paper);box-shadow:0 3px 8px rgba(0,0,0,.25)}
  .welcome{position:absolute;left:21px;top:16px;width:686px}
  .welcome h2{font-family:"PT Sans",sans-serif;font-weight:400;font-size:27px;line-height:1.2;color:var(--ink)}
  .welcome h2 span,.box h3 span{color:var(--red)}
  .welcome p{font-size:12.5px;line-height:1.45;color:var(--ink-soft);margin-top:8px}
  .box{position:absolute;top:150px;width:330px;height:158px;background:linear-gradient(#f3f3f3,#fff);border:1px solid #ddd}
  .box.promotion{left:21px}.box.request{left:377px}
  .box h3{font-family:"PT Sans",sans-serif;font-weight:400;font-size:21px;padding:6px 14px;border-bottom:1px solid #ddd}
  .box p{font-size:12px;line-height:1.5;color:var(--ink-soft);padding:10px 14px}
  .news{position:absolute;left:721px;top:6px;width:253px;height:297px;background:linear-gradient(var(--red-bright),var(--red));border:2px solid #e6e6e6;box-shadow:0 0 0 1px #999;padding:10px 16px;color:#fff}
  .news h3{font-family:"PT Sans",sans-serif;font-size:17px;font-weight:700;padding-bottom:8px;border-bottom:1px solid rgba(255,255,255,.4)}
  .news h3 span{color:#f4d36a}
  .news-item{margin-top:16px;font-size:12.5px;line-height:1.45}
  .news-date{display:flex;align-items:center;gap:8px;font-weight:700;margin-bottom:4px}
  .news-date i{width:11px;height:11px;background:#fff;display:block}

  .site-footer{position:absolute;left:97px;top:855px;width:981px;height:105px;background:linear-gradient(#2c2c2c,var(--footer));color:#ccc}
  .footer-brand{position:absolute;left:24px;top:34px;display:flex;align-items:center;gap:10px}
  .footer-brand .brand-mark{width:28px;height:28px;background:#888}
  .footer-brand .brand-name{font-size:19px}
  .footer-brand .brand-tagline{font-size:11px;color:#aaa}
  .copyright{position:absolute;left:340px;top:44px;font-size:13px}
  .social{position:absolute;right:28px;top:38px;display:flex;gap:8px}
  .social span{width:30px;height:30px;border-radius:4px;background:#3c78b8}
</style>
</head>
<body>
  <div class="header-band"></div>

  <header>
    <div class="brand">
      <div class="brand-mark"></div>
      <div>
        <div class="brand-name">Harbinwell Press</div>
        <div class="brand-tagline">Book Publishing &amp; Printing Services</div>
      </div>
    </div>
    <div class="call">
      <div class="call-label">Call Us Today!</div>
      <div class="call-number">
        <svg width="28" height="30" viewBox="0 0 24 24" aria-hidden="true"><path fill="#8fd13a" d="M6.6 10.8a15 15 0 0 0 6.6 6.6l2.2-2.2a1 1 0 0 1 1-.25 11.4 11.4 0 0 0 3.6.57 1 1 0 0 1 1 1V20a1 1 0 0 1-1 1A17 17 0 0 1 3 4a1 1 0 0 1 1-1h3.5a1 1 0 0 1 1 1c0 1.25.2 2.45.57 3.57a1 1 0 0 1-.25 1z"/></svg>
        1-888-555-0142
      </div>
    </div>
    <nav class="main-nav">
      <a class="active" href="#">Home</a>
      <a href="#">Make Books</a>
      <a href="#">View Library</a>
      <a href="#">Pricing</a>
      <a href="#">Contact Us</a>
    </nav>
  </header>

  <section class="showcase">
    <div class="slide-photo" role="img" aria-label="Photo of printed book pages running through a printing press"></div>
    <div class="slide-arrow prev"><svg width="24" height="24" viewBox="0 0 24 24"><path d="M15 6l-6 6 6 6" stroke="#fff" stroke-width="2.5" fill="none"/></svg></div>
    <div class="slide-arrow next"><svg width="24" height="24" viewBox="0 0 24 24"><path d="M9 6l6 6-6 6" stroke="#fff" stroke-width="2.5" fill="none"/></svg></div>
    <div class="slide-dots"><span></span><span></span><span></span><span></span><span></span></div>
    <div class="showcase-copy">
      <h1>Not All Yearbook Companies Are The Same</h1>
      <p>Harbinwell is a specialized yearbook company, dedicated to revolutionizing how easy and affordable school yearbooks are made! Our next generation of yearbook services includes everything you will need to create great high school yearbooks, elementary school yearbooks, military yearbooks, or any yearbook project!</p>
    </div>
    <a class="cta tour" href="#">Video Tour</a>
    <a class="cta sample" href="#">Request FREE Sample</a>
  </section>

  <main class="content">
    <div class="welcome">
      <h2>Welcome to <span>Harbinwell Press</span></h2>
      <p>Searching for yearbook publishers who combine ease of use, affordability, top-notch service and still deliver a high quality product? One yearbook printing company stands out from the rest... Harbinwell Classbooks. Harbinwell works with high schools, middle schools, elementary schools, colleges/ universities, military groups and churches around the country to fulfill their yearbook publishing needs.</p>
    </div>
    <div class="box promotion">
      <h3>This Month's <span>Promotion</span></h3>
      <p>Lorem ipsum dolor sit amet, consectetur adipisicing elit, sed do eiusmod tempor incididunt ut labore et dolore magna aliqua. Ut enim ad minim veniam, quis nostrud exercitation ullamco labore nisi ut aliquip ex ea commodo consequat.</p>
    </div>
    <div class="box request">
      <h3>Request <span>Information</span></h3>
      <p>Lorem ipsum dolor sit amet, consectetur adipisicing elit, sed do eiusmod tempor incididunt ut labore et dolore magna aliqua. Ut enim ad minim veniam, quis nostrud exercitation ullamco labore nisi ut aliquip ex ea commodo consequat.</p>
    </div>
    <aside class="news">
      <h3>News <span>&amp;</span> Announcements</h3>
      <div class="news-item"><div class="news-date"><i></i>30-5-2011</div>Lorem ipsum dolor sit amet, consectetur adipisicing elit sed do</div>
      <div class="news-item"><div class="news-date"><i></i>20-5-2011</div>Lorem ipsum dolor sit amet, consectetur adipisicing elit sed do</div>
      <div class="news-item"><div class="news-date"><i></i>10-6-2011</div>Lorem ipsum dolor sit amet, consectetur adipisicing elit sed do</div>
    </aside>
  </main>

  <footer class="site-footer">
    <div class="footer-brand">
      <div class="brand-mark"></div>
      <div>
        <div class="brand-name">Harbinwell Press</div>
        <div class="brand-tagline">Book Publishing &amp; Printing Services</div>
      </div>
    </div>
    <div class="copyright">Copyright © 2011 Harbinwell Press. All rights reserved.</div>
    <div class="social" aria-label="Social links"><span></span><span></span><span></span></div>
  </footer>
</body>
</html>
```